I am looking for help designing my new business cards. I would like rounded edges and a raised logo on the back of the card. I have 2 Logos. One with a boat in it and one without. I'd like the one on the back to be the one that includes the boat and just the name on the front. I have included multiple formats of my logo. Please let me know if you need anymore.

Target Market(s)

Potential buyers and other sales brokers

Industry/Entity Type

Sales - Yacht / Boat Sales

Contact Information for Business Card

Id liike the front to include just the business name portion of the logo along with my name (Wesley Corman), phone number (555.318.9062), website address (www.cormanmarinetrade.com) and not my physical address but just "Charleston, SC". The back should include my full logo that has the boat included. This portion I'd prefer raised amd take up the majority of the space there. Thanks!!

Colors
0054AA
0677BA
7BADD7
CADEEF
E8F1F8
0094D4
00A9DD
6FCCEA
C7EBF8
E9F6FB

Requirements
Must have
• Double sided
Nice to have
• My email address: Wesley@cormanmarinetrade.com The NMTG logo somewhere small on the front of the card
Should not have
• My full address, prefer only "Charleston, SC"

```html
<!DOCTYPE html>
<html lang="en">
<head>
<meta charset="utf-8">
<title>Corman Marine Trade – Business Cards</title>
<link rel="stylesheet" href="https://fonts.googleapis.com/css2?family=Montserrat:wght@400;500;700;800&display=swap">
<style>
  :root {
    --page: #ededed;
    --navy: #002a62;
    --ink-navy: #0b2c6b;
    --marine: #0677ba;
    --sky: #0094d4;
    --white: #ffffff;
    --card-w: 500px;
    --card-h: 280px;
  }
  * { box-sizing: border-box; margin: 0; padding: 0; }
  html, body {
    width: 1200px; height: 735px; overflow: hidden;
    background: var(--page);
    font-family: "Montserrat", sans-serif;
  }
  .sheet {
    position: relative; width: 1200px; height: 735px;
    display: flex; align-items: center; justify-content: center; gap: 60px;
  }
  .card {
    position: relative; width: var(--card-w); height: var(--card-h);
    overflow: hidden;
    box-shadow: 0 18px 30px rgba(0,0,0,0.14);
  }

  /* Back of card – navy */
  .card--back {
    background: var(--navy);
    border-radius: 16px 130px 16px 130px;
  }
  .card--back .brand-name {
    position: absolute; top: 34px; right: 56px;
    font-weight: 800; font-size: 25px; letter-spacing: 0.5px;
    color: var(--white); text-transform: uppercase;
  }
  .card--back .boat-art {
    position: absolute; left: 40px; top: 82px; width: 420px; height: 140px;
    border-radius: 10px;
    background: linear-gradient(160deg, rgba(255,255,255,0.18) 0%, rgba(255,255,255,0.06) 45%, var(--marine) 100%);
  }
  .card--back .website {
    position: absolute; right: 48px; bottom: 22px;
    font-size: 12.5px; font-weight: 400; letter-spacing: 3px;
    color: var(--white);
  }

  /* Front of card – white */
  .card--front {
    background: var(--white);
    border-radius: 130px 16px 130px 16px;
  }
  .contact {
    position: absolute; left: 30px; top: 96px; width: 170px;
    text-align: right; color: var(--ink-navy);
    font-size: 12px; letter-spacing: 2.4px; line-height: 1.6;
  }
  .contact .person {
    font-weight: 800; font-size: 12.5px; letter-spacing: 2.6px;
  }
  .divider {
    position: absolute; left: 216px; top: 30px;
    width: 2px; height: 220px; background: var(--marine);
  }
  .mark {
    position: absolute; left: 240px; top: 42px; width: 230px;
    display: flex; flex-direction: column; align-items: center; gap: 10px;
  }
  .mark .boat-art {
    width: 200px; height: 100px; border-radius: 8px;
    background: linear-gradient(170deg, #e8f1f8 0%, #7badd7 60%, var(--sky) 100%);
  }
  .mark .brand-name {
    font-weight: 800; font-size: 22px; letter-spacing: 0.5px;
    color: var(--ink-navy); text-transform: uppercase; text-align: center; line-height: 1.15;
  }
</style>
</head>
<body>
  <main class="sheet">
    <section class="card card--back" aria-label="Business card back">
      <div class="brand-name">Corman Marine Trade</div>
      <div class="boat-art" role="img" aria-label="Illustration of a center-console fishing boat riding a blue wave"></div>
      <div class="website">www.cormanmarinetrade.com</div>
    </section>

    <section class="card card--front" aria-label="Business card front">
      <div class="contact">
        <p class="person">Wesley Corman</p>
        <p>555.318.9062</p>
        <p>Charleston, SC</p>
      </div>
      <div class="divider"></div>
      <div class="mark">
        <div class="boat-art" role="img" aria-label="Small illustration of a fishing boat over a blue wave"></div>
        <div class="brand-name">Corman<br>Marine Trade</div>
      </div>
    </section>
  </main>
</body>
</html>
```